Looking for Desginers for an abstract art canvas & poster stallcraft shop

I want to get a design done for an abstract canvas art & print shop. If possible im looking to create the design based on the harbor or quarry template (im open to suggestions). Mostly I need the creative assets such as banners, images, copywriting, typography etc since im having a hard time to give it a descent look myself.

Target Market(s)

Home decor lovers, abstract art enthusiasts and canvas art enthusiast

Industry/Entity Type

Art

Coding

Coded - Design and coding required

Number of Pages Required

1 page

Colors

Designer to choose only greyscale colors for use in the design.

Requirements
Must have
• Creatives Assets such as banners, images, copy, collection image templates. Please use the velunor logo provided below in at least one of the proposals.
Should not have
• anything that has to be coded into html or css.

```html
<!DOCTYPE html>
<html lang="en">
<head>
<meta charset="utf-8">
<title>velunor — Abstract Art Canvas &amp; Posters</title>
<link href="https://fonts.googleapis.com/css2?family=Lora:wght@400;500&family=Lato:wght@400;700&display=swap" rel="stylesheet">
<style>
:root{
  --ink:#111111;
  --text:#333333;
  --muted:#777777;
  --line:#cfcfcf;
  --paper:#ffffff;
  --band:#efefef;
  --star:#f2b01e;
}
*{margin:0;padding:0;box-sizing:border-box}
html,body{width:1200px;height:3276px;overflow:hidden;background:var(--paper)}
body{position:relative;font-family:"Lato",Arial,sans-serif;color:var(--text)}
.abs{position:absolute}
.serif{font-family:"Lora",Georgia,serif}

/* header */
.site-header{left:0;top:0;width:1200px;height:60px;z-index:2}
.brand{left:0;width:1200px;top:14px;text-align:center;font-family:"Lora",Georgia,serif;font-size:24px;color:var(--ink);letter-spacing:1px}
.header-icon{top:20px}

/* hero */
.hero{left:0;top:0;width:1200px;height:560px;background:radial-gradient(ellipse at 40% 40%,#fafafa 0%,#e6e6e6 55%,#d2d2d2 100%)}
.hero-title{left:0;width:1200px;top:210px;text-align:center;font-size:42px;color:var(--ink)}
.hero-sub{left:0;width:1200px;top:272px;text-align:center;font-size:11px;font-weight:700;letter-spacing:1px;color:var(--ink)}
.btn{display:flex;align-items:center;justify-content:center;background:var(--ink);color:#fff;font-size:10px;font-weight:700;letter-spacing:1px}
.hero-btn{left:536px;top:318px;width:128px;height:36px}
.dots{left:572px;top:525px;display:flex;gap:12px}
.dot{width:10px;height:10px;border-radius:50%;border:1.5px solid var(--ink)}
.dot.on{background:var(--ink)}

.intro{left:350px;width:500px;top:620px;text-align:center;font-size:12.5px;line-height:1.75;color:var(--muted)}
.intro a{color:var(--ink);text-decoration:underline}
.rule{height:1px;background:#999}

.section-title{left:0;width:1200px;text-align:center;font-size:34px;color:var(--ink)}

/* featured */
.tile{overflow:hidden}
.tile-shade{position:absolute;inset:0;background:rgba(0,0,0,.35)}
.tile-name{position:absolute;left:0;right:0;top:44%;text-align:center;color:#fff;font-family:"Lora",Georgia,serif;font-size:18px}
.tile-price{position:absolute;left:18px;bottom:16px;color:#fff;font-size:22px}
.tile-rate{position:absolute;right:16px;bottom:16px;text-align:center;color:#fff;font-size:9px;line-height:1.3}
.stars{color:var(--star);font-size:13px;letter-spacing:1px}

/* style grid */
.style-card{text-align:center;font-size:12px;color:var(--text)}
.style-img{width:252px;height:188px}
.style-name{margin-top:12px;font-size:12px;color:var(--ink)}
.style-card .stars{display:block;margin-top:4px}
.style-rev{font-size:9px;color:var(--muted)}

/* award */
.award-art{left:172px;top:2212px;width:408px;height:440px;background:#efefef}
.poster{left:96px;top:40px;width:216px;height:344px;background:#fff;box-shadow:0 1px 3px rgba(0,0,0,.15)}
.poster-img{position:absolute;left:24px;top:24px;width:168px;height:216px;background:linear-gradient(135deg,#111 0%,#2a2a2a 60%,#111 100%)}
.poster-title{position:absolute;left:0;right:0;top:262px;text-align:center;font-family:"Lora",Georgia,serif;font-size:20px;letter-spacing:3px;color:var(--ink)}
.poster-sub{position:absolute;left:0;right:0;top:296px;text-align:center;font-family:"Lora",Georgia,serif;font-size:11px;letter-spacing:4px;color:var(--muted)}
.award-copy{left:672px;top:2250px;width:340px}
.award-copy h2{font-family:"Lora",Georgia,serif;font-weight:500;font-size:29px;line-height:1.3;color:var(--ink)}
.award-copy .kicker{margin-top:14px;font-size:10px;font-weight:700;letter-spacing:1px;color:var(--ink)}
.award-copy p{margin-top:18px;font-size:11.5px;line-height:1.7;color:var(--muted)}
.award-copy .btn{margin-top:26px;width:130px;height:34px}

/* newsletter */
.newsletter{left:0;top:2640px;width:1200px;height:228px;background:var(--band)}
.news-title{left:0;width:1200px;top:40px;text-align:center;font-size:28px;color:var(--ink)}
.news-sub{left:0;width:1200px;top:84px;text-align:center;font-size:10px;font-weight:700;letter-spacing:1px;color:var(--ink)}
.news-field{left:380px;top:152px;width:320px;height:36px;background:#fff;font-size:10px;color:#aaa;padding:12px 14px}
.news-btn{left:700px;top:152px;width:120px;height:36px}

/* footer */
.footer-col{top:3092px;font-size:11px;line-height:20px;color:var(--text)}
.social li{list-style:none;display:flex;align-items:center;gap:10px}
.social .mark{width:7px;height:7px;border-radius:50%;background:var(--ink)}
</style>
</head>
<body>

<section class="hero abs" role="img" aria-label="White abstract brush stroke texture painting"></section>

<header class="site-header abs">
  <svg class="header-icon abs" style="left:40px" width="18" height="14" viewBox="0 0 18 14"><path d="M0 1h18M0 7h18M0 13h18" stroke="#111" stroke-width="1.6"/></svg>
  <div class="brand abs">velunor</div>
  <svg class="header-icon abs" style="left:1080px" width="16" height="16" viewBox="0 0 16 16"><circle cx="6.5" cy="6.5" r="5" fill="none" stroke="#111" stroke-width="1.6"/><path d="M10.5 10.5L15 15" stroke="#111" stroke-width="1.6"/></svg>
  <svg class="header-icon abs" style="left:1114px" width="18" height="16" viewBox="0 0 18 16"><path d="M0 1h3l2 9h10l2-7H5" fill="none" stroke="#111" stroke-width="1.6"/><circle cx="7" cy="14" r="1.4" fill="#111"/><circle cx="14" cy="14" r="1.4" fill="#111"/></svg>
  <svg class="header-icon abs" style="left:1148px" width="14" height="16" viewBox="0 0 14 16"><rect x="1" y="4" width="12" height="11" fill="none" stroke="#111" stroke-width="1.6"/><path d="M4 4V2h6v2" fill="none" stroke="#111" stroke-width="1.6"/></svg>
</header>

<h1 class="hero-title abs serif" style="font-weight:400">The Beauty of true Art</h1>
<div class="hero-sub abs">BEAUTIFUL &amp; ATTRACTIVE ABSTRACT ART CANVAS AND POSTERS</div>
<div class="btn hero-btn abs">EXPLORE NOW</div>
<svg class="abs" style="left:168px;top:523px" width="16" height="14" viewBox="0 0 16 14"><path d="M15 7H2M7 1L1 7l6 6" fill="none" stroke="#111" stroke-width="1.6"/></svg>
<svg class="abs" style="left:1016px;top:523px" width="16" height="14" viewBox="0 0 16 14"><path d="M1 7h13M9 1l6 6-6 6" fill="none" stroke="#111" stroke-width="1.6"/></svg>
<div class="dots abs"><span class="dot on"></span><span class="dot"></span></div>

<p class="intro abs">Our products are inspired by the people and world around us. Beautiful, high quality art and posters that are designed especially for you. Discover <a>our range</a> and meet the people that make our brand what it is.</p>
<div class="rule abs" style="left:580px;top:705px;width:40px"></div>

<h2 class="section-title abs serif" style="top:770px;font-weight:400">Featured Collection</h2>
<div class="rule abs" style="left:580px;top:828px;width:40px"></div>

<div class="tile abs" style="left:172px;top:888px;width:400px;height:220px;background:linear-gradient(135deg,#3a3a3a,#9a9a9a 50%,#2b2b2b)" role="img" aria-label="Black and white abstract canvas">
  <div class="tile-shade"></div><div class="tile-name">Black &amp; White Abstract</div><div class="tile-price">$30</div>
  <div class="tile-rate"><span class="stars">★★★★★</span><br>(20 reviews)</div>
</div>
<div class="tile abs" style="left:612px;top:888px;width:416px;height:220px;background:linear-gradient(135deg,#c9c2b5,#c23a2a 35%,#1f3f8a 60%,#e0c23a 85%)" role="img" aria-label="Colorful abstract canvas">
  <div class="tile-shade"></div><div class="tile-name">Colorful</div><div class="tile-price">$50</div>
  <div class="tile-rate"><span class="stars">★★★★★</span><br>(20 reviews)</div>
</div>
<div class="tile abs" style="left:172px;top:1140px;width:268px;height:220px;background:linear-gradient(160deg,#bdbdbd,#4a4a4a 55%,#1a1a1a)" role="img" aria-label="Black and white abstract portrait artwork">
  <div class="tile-shade"></div><div class="tile-name">Black &amp; White Abstract</div><div class="tile-price">$90</div>
  <div class="tile-rate"><span class="stars">★★★★★</span><br>(20 reviews)</div>
</div>
<div class="tile abs" style="left:468px;top:1140px;width:264px;height:220px;background:radial-gradient(circle at 50% 40%,#3c4a5a,#141a22 70%)" role="img" aria-label="Dark galaxy themed artwork">
  <div class="tile-shade"></div><div class="tile-name">Galaxy</div><div class="tile-price">$70</div>
  <div class="tile-rate"><span class="stars">★★★★★</span><br>(20 reviews)</div>
</div>
<div class="tile abs" style="left:760px;top:1140px;width:268px;height:220px;background:linear-gradient(135deg,#2f6b5a,#c8763a 45%,#7a3a6a 75%,#2a4a7a)" role="img" aria-label="Colorful street art mural">
  <div class="tile-shade"></div><div class="tile-name">Street</div><div class="tile-price">$80</div>
  <div class="tile-rate"><span class="stars">★★★★★</span><br>(20 reviews)</div>
</div>

<h2 class="section-title abs serif" style="top:1450px;font-weight:400">Search by Style</h2>
<div class="rule abs" style="left:580px;top:1508px;width:40px"></div>

<div class="style-card abs" style="left:172px;top:1552px">
  <div class="style-img" style="border:1px solid #ddd;background:radial-gradient(circle at 50% 45%,#9a9a9a,#f4f4f4 70%)" role="img" aria-label="Black and white botanical line art"></div>
  <div class="style-name">Black &amp; White</div><span class="stars">★★★★★</span><div class="style-rev">(20 reviews)</div>
</div>
<div class="style-card abs" style="left:472px;top:1552px">
  <div class="style-img" style="background:linear-gradient(135deg,#1f4a2e,#4c8a4a 50%,#1b3a24)" role="img" aria-label="Green tropical leaves artwork"></div>
  <div class="style-name">Natural</div><span class="stars">★★★★★</span><div class="style-rev">(20 reviews)</div>
</div>
<div class="style-card abs" style="left:776px;top:1552px">
  <div class="style-img" style="background:linear-gradient(135deg,#e8c0a8,#d8453a 40%,#2a8a7a 75%,#f0d890)" role="img" aria-label="Colorful geometric wall art"></div>
  <div class="style-name">Wall Art</div><span class="stars">★★★★★</span><div class="style-rev">(20 reviews)</div>
</div>
<div class="style-card abs" style="left:172px;top:1844px">
  <div class="style-img" style="background:linear-gradient(135deg,#1c4aa0,#d83a2a 45%,#f0a030 70%,#2a2a6a)" role="img" aria-label="Colorful abstract paint strokes"></div>
  <div class="style-name">Colorful</div><span class="stars">★★★★★</span><div class="style-rev">(20 reviews)</div>
</div>
<div class="style-card abs" style="left:472px;top:1844px">
  <div class="style-img" style="background:linear-gradient(160deg,#8aa8b0,#3a6a6a 50%,#a07a5a)" role="img" aria-label="Modern urban mural artwork"></div>
  <div class="style-name">Modern</div><span class="stars">★★★★★</span><div class="style-rev">(20 reviews)</div>
</div>
<div class="style-card abs" style="left:776px;top:1844px">
  <div class="style-img" style="background:linear-gradient(135deg,#3a2a2a,#a04a3a 40%,#d8c8a8 70%,#2a2a2a)" role="img" aria-label="Wall of vintage posters"></div>
  <div class="style-name">Poster</div><span class="stars">★★★★★</span><div class="style-rev">(20 reviews)</div>
</div>

<div class="award-art abs">
  <div class="poster abs">
    <div class="poster-img" role="img" aria-label="Black poster with white brush stroke"></div>
    <div class="poster-title">Black &amp; White</div>
    <div class="poster-sub">• Abstract Art •</div>
  </div>
</div>
<div class="award-copy abs">
  <h2>Award winning abstract art and posters.</h2>
  <div class="kicker">WELL RECOGNIZED BY PEOPLE ALL OVER THE GLOBE</div>
  <p>Lorem ipsum dolor sit amet, consectetur sadipscing elitr, sed diam nonumy eirmod tempor invidunt ut labore et dolore magna aliquyam erat, sed diam voluptua.</p>
  <p>At vero eos et accusam et justo duo dolores et ea rebum. Stet clita kasd gubergren, no sea takimata sanctus est. Lorem ipsum dolor sit amet.</p>
  <div class="btn">EXPLORE NOW</div>
</div>

<section class="newsletter abs">
  <h2 class="news-title abs serif" style="font-weight:400">Subscribe to our Newsletter</h2>
  <div class="news-sub abs">SIGN UP FOR OUR EMAIL LIST AND GET 10% OFF YOUR FIRST ORDER</div>
  <div class="rule abs" style="left:580px;top:112px;width:40px"></div>
  <div class="news-field abs">Your email</div>
  <div class="btn news-btn abs">SUBSCRIBE</div>
</section>

<div class="rule abs" style="left:580px;top:2990px;width:40px"></div>

<ul class="footer-col abs" style="left:172px;list-style:none">
  <li>Return Policy</li><li>Search</li><li>Blog</li><li>Contact us</li><li>About us</li>
</ul>
<ul class="footer-col social abs" style="left:492px">
  <li><span class="mark"></span>Circlebook</li>
  <li><span class="mark"></span>Photoline</li>
  <li><span class="mark"></span>Chirper</li>
  <li><span class="mark"></span>Pinboard</li>
  <li><span class="mark"></span>Workmesh</li>
</ul>
<ul class="footer-col abs" style="left:812px;list-style:none">
  <li>© 2021, velunor | All Rights Reserved</li><li>Privacy Policy</li><li>Terms &amp; Conditions</li><li>Disclaimer</li>
</ul>

</body>
</html>
```